New web design for a service provider in the medical field

We are looking for a new design for our website. We are a company that repairs and sells medical endoscopes. Our customers include doctors and hospitals. Our current website can be found at https://lumenfix.example/en/lumenfix-english.
We need a new web design (without programming) for the following 3 pages:
-Startpage https://lumenfix.example/en/lumenfix-english/
-Used endoscopes https://lumenfix.example/en/used-endoscopes/
-Purchase https://lumenfix.example/en/purchase/
The design should be modern and stylish.
The blue color of the logo should be reflected on the page, but not too intrusive.
I have uploaded the images from the header. If more images are needed, let me know and I will upload them.

Target Market(s)
Doctors and hospitals

```html
<!DOCTYPE html>
<html lang="en">
<head>
<meta charset="utf-8">
<title>LumenFix – Endoscope Repair and Sale</title>
<link href="https://fonts.googleapis.com/css2?family=Mulish:wght@400;600;700;800;900&display=swap" rel="stylesheet">
<style>
:root{
  --blue:#0c4ea3;
  --blue-dark:#0a3f86;
  --blue-soft:#e4eef8;
  --blue-mid:#1a6fc2;
  --ink:#1e2a38;
  --text:#3a4452;
  --white:#ffffff;
  --footer:#1f1f20;
  --footer-line:#4a4a4c;
}
*{box-sizing:border-box;margin:0;padding:0}
html,body{width:1200px;height:3930px;overflow:hidden}
body{font-family:"Mulish",Arial,sans-serif;color:var(--text);background:var(--white);position:relative}
a{color:inherit;text-decoration:none}
.section{position:absolute;left:0;width:1200px}
.abs{position:absolute}
.upper{text-transform:uppercase}
.btn{display:inline-flex;align-items:center;justify-content:center;background:var(--blue);color:var(--white);font-weight:800;font-size:11.5px;letter-spacing:.3px;text-transform:uppercase}

/* top bar */
.topbar{top:0;height:26px;background:var(--blue);color:var(--white);font-size:10px;font-weight:700}
.topbar .follow{left:131px;top:7px;display:flex;align-items:center;gap:8px}
.social-dot{width:12px;height:12px;border-radius:50%;background:var(--white);display:inline-block}
.social-sq{width:12px;height:12px;border:2px solid var(--white);border-radius:3px;display:inline-block}
.topbar .links{right:133px;top:7px;display:flex}
.topbar .links a{padding:0 12px;border-left:1px solid rgba(255,255,255,.5)}
.topbar .links a:first-child{border-left:none}
.topbar .links a:last-child{padding-right:0}

/* header */
.header{top:26px;height:104px;background:var(--white)}
.brand{left:140px;top:38px;display:flex;align-items:center;gap:8px;font-size:22px;font-weight:800;color:var(--ink)}
.brand-dot{width:14px;height:14px;border-radius:50%;background:var(--blue-mid)}
.contact{top:22px;display:flex;align-items:center;gap:9px;color:var(--ink)}
.contact .ico{width:22px;height:22px;border-radius:50%;background:var(--blue);display:flex;align-items:center;justify-content:center}
.contact small{display:block;font-size:9px;font-weight:700;text-transform:uppercase}
.contact b{font-size:15px;font-weight:600}
.lang{left:996px;top:23px;width:71px;height:27px;border:1px solid #c3c9d2;display:flex;align-items:center;gap:6px;padding-left:8px;font-size:11px;font-weight:700;color:var(--ink)}
.flag{width:15px;height:10px;background:linear-gradient(#111 0 33%,#d40000 33% 66%,#f6c500 66%)}
.nav{left:304px;top:72px;display:flex;gap:0;font-size:11.5px;font-weight:600;color:var(--ink)}
.nav a{position:absolute;white-space:nowrap}
.nav a.active{color:var(--blue);border-bottom:2px solid var(--blue);padding-bottom:4px}

/* hero */
.hero{top:130px;height:550px;background:linear-gradient(115deg,#d8c6cf 0%,#e7e4ea 25%,#cfd6e2 55%,#aeb8c8 100%)}
.hero-box{left:134px;top:171px;width:423px;height:168px;background:rgba(70,70,74,.72);padding:20px 26px}
.hero-box h1{color:var(--white);font-size:29px;line-height:36px;font-weight:900;text-transform:uppercase}
.hero-box .btn{margin-top:16px;width:122px;height:41px;border:2px solid var(--white);font-size:13px}
.dots{left:567px;top:502px;display:flex;gap:7px}
.dots i{width:11px;height:11px;border-radius:50%;border:1.5px solid var(--white);display:block}
.dots i.on{background:var(--blue);border-color:var(--white)}

/* services */
.services{top:680px;height:412px}
.service{top:52px;width:260px;text-align:center;transform:translateX(-50%)}
.service svg{display:block;margin:0 auto 22px}
.service h3{color:var(--blue);font-size:18px;font-weight:800;text-transform:uppercase}
.service .sub{font-size:14px;color:var(--ink);margin-top:4px}
.service p{font-size:11.5px;line-height:16px;margin-top:20px;height:80px}
.service .btn{margin-top:18px;height:32px;padding:0 15px}

/* intro */
.intro{top:1092px;height:397px;background:var(--blue-soft)}
.intro-rule{top:-4px;left:0;width:1200px;height:6px;background:linear-gradient(90deg,#6f9fd1 0%,#a9c6e6 30%,var(--blue-soft) 100%);clip-path:polygon(0 0,100% 100%,0 100%)}
.intro-photo{left:130px;top:55px;width:444px;height:299px;background:linear-gradient(135deg,#eef1f4 0%,#c8ccd2 45%,#6f7178 70%,#c2b49a 100%)}
.intro-text{left:620px;top:54px;width:450px}
.intro-text h2{color:var(--blue);font-size:20px;line-height:26px;font-weight:800;text-transform:uppercase}
.intro-text p{font-size:13.5px;line-height:21px;color:var(--ink);margin-top:20px}
.intro-text p:first-of-type{margin-top:38px}

/* features */
.features{top:1489px;height:798px;background:var(--blue);color:var(--white)}
.features h2{top:48px;width:1200px;text-align:center;font-size:19px;font-weight:800;text-transform:uppercase}
.features .line{top:92px;left:583px;width:35px;height:2px;background:var(--white)}
.feature{width:455px;height:162px;border:1.5px solid rgba(255,255,255,.85);display:flex;align-items:center;padding:0 24px 0 26px;gap:22px}
.feature svg{flex:none}
.feature h3{font-size:16px;font-weight:800;text-transform:uppercase;line-height:21px}
.feature p{font-size:12px;line-height:17px;margin-top:9px}
.features .btn{left:472px;top:719px;width:256px;height:38px;background:#1268bd}

/* future */
.future{top:2287px;height:451px;background:var(--white)}
.future-left{left:0;top:0;width:330px;height:451px;background:linear-gradient(160deg,#fff 0%,#f0f0f0 40%,#2a2a2c 70%,#111 100%)}
.future-box{left:330px;top:75px;width:426px;height:301px;background:var(--blue-soft);padding:30px 42px}
.future-box h2{color:var(--blue);font-size:30px;line-height:38px;font-weight:800;text-transform:uppercase}
.future-box p{font-size:13.5px;line-height:21px;color:var(--ink);margin-top:30px;padding-left:4px}
.future-right{left:756px;top:100px;width:444px;height:351px;background:linear-gradient(200deg,#ffffff 0%,#d9dde2 30%,#1c1d22 60%,#0a0a0c 100%)}

/* faulty */
.faulty{top:2738px;height:237px;background:linear-gradient(180deg,#eaf1f9,#dbe7f4)}
.faulty h2{top:43px;width:1200px;text-align:center;color:var(--blue);font-size:29px;font-weight:800;text-transform:uppercase}
.faulty .lead{top:94px;width:1200px;text-align:center;font-size:17px;color:var(--ink)}
.pickup{left:452px;top:136px;display:flex;height:39px}
.pickup .field{width:151px;border:1.5px solid var(--blue);background:var(--white);color:var(--blue);font-size:16px;display:flex;align-items:center;padding-left:13px}
.pickup .btn{width:150px;font-size:13.5px}

/* outcome */
.outcome{top:2975px;height:633px}
.outcome-photo{left:0;top:0;width:586px;height:633px;background:linear-gradient(135deg,#f3f3f3 0%,#bfc1c5 35%,#3a3b3f 60%,#d8d8da 100%)}
.outcome-list{left:629px;top:47px;width:470px}
.outcome-list h2{color:var(--blue);font-size:20px;font-weight:800;text-transform:uppercase}
.point{position:absolute;left:0;display:flex;gap:16px;width:480px}
.point svg{flex:none;margin-top:2px}
.point h3{color:var(--blue);font-size:14px;font-weight:800;text-transform:uppercase}
.point p{font-size:13.5px;line-height:20px;color:var(--ink);margin-top:3px}

/* footer */
.footer{top:3608px;height:322px;background:var(--footer);color:var(--white)}
.footer-brand{left:137px;top:74px;display:flex;align-items:center;gap:10px;font-size:32px;font-weight:800}
.footer-brand .brand-dot{width:18px;height:18px;background:#2a8ee0}
.fcol{top:43px}
.fcol h4{color:#3d93e3;font-size:11.5px;font-weight:800;text-transform:uppercase;margin-bottom:17px}
.fcol a{display:block;font-size:12px;line-height:22.5px;text-transform:uppercase}
.fsocial{display:flex;gap:12px;align-items:center}
.fsocial .social-dot{width:28px;height:28px}
.fsocial .social-sq{width:30px;height:30px;border-width:3px;border-radius:7px}
.footer .rule{left:133px;top:237px;width:934px;height:1px;background:var(--footer-line)}
.footer .copy{top:278px;width:1200px;text-align:center;font-size:12px}
</style>
</head>
<body>

<div class="section topbar">
  <div class="abs follow">FOLLOW US <span class="social-dot" aria-label="Social profile"></span><span class="social-sq" aria-label="Social profile"></span></div>
  <nav class="abs links"><a href="#">PICK-UP ORDER</a><a href="#">ABOUT US</a><a href="#">CONTACT US</a></nav>
</div>

<header class="section header">
  <a class="abs brand" href="https://lumenfix.example/en/lumenfix-english/"><span class="brand-dot"></span>LumenFix</a>
  <div class="abs contact" style="left:591px">
    <span class="ico"><svg width="12" height="10" viewBox="0 0 12 10"><rect x="0.5" y="0.5" width="11" height="9" rx="1" fill="none" stroke="#fff"/><path d="M1 1l5 4 5-4" fill="none" stroke="#fff"/></svg></span>
    <div><small>Email us</small><b>info@lumenfix.example</b></div>
  </div>
  <div class="abs contact" style="left:795px">
    <span class="ico"><svg width="12" height="12" viewBox="0 0 12 12"><path d="M3 1l2 2.5-1.2 1.3a7 7 0 0 0 3.4 3.4L8.5 7 11 9l-1.3 2A9 9 0 0 1 1 2.3z" fill="#fff"/></svg></span>
    <div><small>Call us</small><b>+49 4100 555 010-0</b></div>
  </div>
  <div class="abs lang"><span class="flag"></span>DE <svg width="8" height="5" viewBox="0 0 8 5" style="margin-left:6px"><path d="M0 0h8L4 5z" fill="#1e2a38"/></svg></div>
  <nav class="abs nav">
    <a class="active" href="https://lumenfix.example/en/lumenfix-english/" style="left:0">HOME</a>
    <a href="#" style="left:66px">ENDOSCOPE REPAIR</a>
    <a href="https://lumenfix.example/en/used-endoscopes/" style="left:211px">USED ENDOSCOPES</a>
    <a href="#" style="left:353px">ENDOSCOPY SYSTEMS</a>
    <a href="#" style="left:513px">ENDOSCOPY ACCESSORIES</a>
    <a href="https://lumenfix.example/en/purchase/" style="left:697px">PURCHASE</a>
  </nav>
</header>

<section class="section hero" role="img" aria-label="Photo of a flexible endoscope with its control head lying on a white surgical drape">
  <div class="abs hero-box">
    <h1>Put your endoscope<br>in reliable hands!</h1>
    <a class="btn" href="#">Read more</a>
  </div>
  <div class="abs dots"><i></i><i class="on"></i><i></i><i></i></div>
</section>

<section class="section services">
  <div class="abs service" style="left:255px">
    <svg width="72" height="66" viewBox="0 0 72 66" fill="none" stroke="#0c4ea3" stroke-width="2.5" stroke-linejoin="round"><path d="M14 6a10 10 0 0 0 10 14l24 24a6 6 0 0 0 8-8L32 12A10 10 0 0 0 18 2l6 6-2 6-6 2z"/><path d="M60 4l6 6-24 24-6-6z"/><path d="M30 34L12 52l4 4 18-18"/></svg>
    <h3>Repair</h3>
    <div class="sub">Endoscope repair service</div>
    <p>Manufacturer-independent we repair and maintain endoscopes, individual components (e.g. processors or light sources), accessories and peripherals of the manufacturers Olvara, Pentrix and Fujiro.</p>
    <a class="btn" href="#">Repair request</a>
  </div>
  <div class="abs service" style="left:605px">
    <svg width="66" height="66" viewBox="0 0 66 66" fill="none" stroke="#0c4ea3" stroke-width="3"><circle cx="33" cy="36" r="26"/><circle cx="33" cy="36" r="17"/><path d="M20 12V3h10v8"/></svg>
    <h3>Sale</h3>
    <div class="sub">Used endoscopes</div>
    <p>Our regular stock includes refurbished gastroscopes, coloscopes, bronchoscopes, cystoscopes and duodenoscopes from the well-known manufacturers Olvara, Pentrix and Fujiro.</p>
    <a class="btn" href="https://lumenfix.example/en/used-endoscopes/">Purchase request</a>
  </div>
  <div class="abs service" style="left:954px">
    <svg width="70" height="66" viewBox="0 0 70 66" fill="none" stroke="#0c4ea3" stroke-width="2.5" stroke-linejoin="round"><path d="M2 4h10l8 38h40l6-28H14"/><path d="M20 22h44M18 32h44M30 14v28M42 14v28M54 14v28"/><circle cx="26" cy="56" r="5"/><circle cx="54" cy="56" r="5"/></svg>
    <h3>Purchase</h3>
    <div class="sub">Used endoscopes</div>
    <p>We are very interested in buying your old endoscopes – even defective and dismantled! We offer fair conditions! Please contact us for a purchase offer!</p>
    <a class="btn" href="https://lumenfix.example/en/purchase/">Sell device</a>
  </div>
</section>

<section class="section intro">
  <div class="abs intro-rule"></div>
  <div class="abs intro-photo" role="img" aria-label="Photo of an endoscope control head mounted on a holder"></div>
  <div class="abs intro-text">
    <h2>Endoscope repairs and second hand endoscopes from LumenFix – cause the outcome matters!</h2>
    <p>LumenFix is a privileged partner for the start-up facility or optimisation of existing healthcare facilities, doctor's offices and hospitals. The quality and reliability of our products and our offered service are our best advertisement!</p>
    <p>As a result of optimised processes and highly qualified specialists in our company, we can work very quickly and with high quality for your benefit of least possible restrictions in your doctor's office or in your hospital.</p>
  </div>
</section>

<section class="section features">
  <h2 class="abs">LumenFix GmbH, your decision for your future</h2>
  <div class="abs line"></div>

  <div class="abs feature" style="left:131px;top:139px">
    <svg width="78" height="62" viewBox="0 0 78 62" fill="none" stroke="#fff" stroke-width="2.2"><circle cx="30" cy="31" r="12"/><path d="M30 7v7M30 48v7M6 31h7M47 31h7M13 14l5 5M42 43l5 5M13 48l5-5M42 19l5-5"/><path d="M56 22h18M58 31h16M56 40h18"/></svg>
    <div><h3>Fast repairs</h3><p>Keep potential disruptions in your doctor's office or in your hospital at minimum as a result of optimized processes and highly qualified specialists in our company</p></div>
  </div>
  <div class="abs feature" style="left:614px;top:139px">
    <svg width="78" height="66" viewBox="0 0 78 66" fill="none" stroke="#fff" stroke-width="2.2"><circle cx="46" cy="26" r="18"/><path d="M51 17h-7a4 4 0 0 0 0 8h4a4 4 0 0 1 0 8h-8M46 13v4M46 33v4"/><path d="M6 46h8v16H6zM14 48l8-6 4 4h12v8H14"/><path d="M20 6l2 4M12 12l4 2M70 50l-4-2"/></svg>
    <div><h3>Highly cost efficient</h3><p>Benefit from our first class recommendations and implementation by our experienced staff. Our goals is to find the best solutions together with you at the best lowest price point.</p></div>
  </div>
  <div class="abs feature" style="left:131px;top:327px">
    <svg width="78" height="76" viewBox="0 0 78 76" fill="none" stroke="#fff" stroke-width="2.2"><circle cx="39" cy="20" r="16"/><circle cx="39" cy="20" r="9"/><path d="M27 31v24M51 31v24M24 55h6v14h-6zM48 55h6v14h-6z"/></svg>
    <div><h3>On-site service</h3><p>We will gladly pay you a visit to carry out analysis and repairs on site. Due to our many years of experience – it doesn't get any faster (within a 250 km range)</p></div>
  </div>
  <div class="abs feature" style="left:614px;top:327px">
    <svg width="78" height="76" viewBox="0 0 78 76" fill="none" stroke="#fff" stroke-width="2.2"><rect x="14" y="4" width="50" height="68" rx="4"/><rect x="21" y="12" width="36" height="12"/><rect x="21" y="32" width="15" height="14"/><rect x="42" y="32" width="15" height="14"/><rect x="21" y="52" width="15" height="14"/><rect x="42" y="52" width="15" height="14"/></svg>
    <div><h3>Loan equipment service</h3><p>Use our service of high-quality loan devices during the downtime of your defective endoscope (limited to stock)</p></div>
  </div>
  <div class="abs feature" style="left:131px;top:514px">
    <svg width="78" height="76" viewBox="0 0 78 76" fill="none" stroke="#fff" stroke-width="2.2"><path d="M14 4h40v34M54 66v4H14V4"/><path d="M22 16h24M22 24h24M22 32h24M22 40h14"/><circle cx="56" cy="54" r="12"/><path d="M50 54l5 5 8-9M20 58c4-6 6 4 10-2"/></svg>
    <div><h3>Without a maintenance contract</h3><p>No subscription or other maintenance contract, but one-time and sustainable repair work</p></div>
  </div>
  <div class="abs feature" style="left:614px;top:514px">
    <svg width="78" height="76" viewBox="0 0 78 76" fill="none" stroke="#fff" stroke-width="2.2" stroke-linejoin="round"><path d="M30 36l8-14c2-6 0-12 4-14 6 0 6 8 4 16h16a5 5 0 0 1 0 10h-2a5 5 0 0 1 0 10h-2a5 5 0 0 1 0 10h-2a5 5 0 0 1 0 10H42c-6 0-10-3-12-4"/><path d="M10 40c6 2 12 2 18 0M10 52c6 2 12 2 18 0"/></svg>
    <div><h3>First class service</h3><p>Our clients always come first!</p></div>
  </div>

  <a class="abs btn" href="#">Learn more about LumenFix!</a>
</section>

<section class="section future">
  <div class="abs future-left" role="img" aria-label="Photo of an endoscope eyepiece with an orange ring"></div>
  <div class="abs future-right" role="img" aria-label="Photo of several endoscope control heads lined up"></div>
  <div class="abs future-box">
    <h2>Your future -<br>our service</h2>
    <p>LumenFix GmbH is specialised in the repair and sale of Olvara, Pentrix and Fujiro flexible medical endoscopes. As a service-oriented company, we are at your side with our knowledge and skills!</p>
  </div>
</section>

<section class="section faulty">
  <h2 class="abs">Faulty endoscope?</h2>
  <div class="abs lead">We ensure quick and smooth repairs!</div>
  <div class="abs pickup">
    <div class="field">Simple place a</div>
    <a class="btn" href="#">Pick-up order</a>
  </div>
</section>

<section class="section outcome">
  <div class="abs outcome-photo" role="img" aria-label="Photo of two flexible endoscopes crossing on a white background"></div>
  <div class="abs outcome-list">
    <h2>Cause the outcome matters!</h2>
    <div class="point" style="top:70px">
      <svg width="38" height="38" viewBox="0 0 38 38" fill="none" stroke="#0c4ea3" stroke-width="2"><circle cx="19" cy="11" r="7"/><path d="M5 36c0-10 6-15 14-15s14 5 14 15zM14 22l5 7 5-7"/></svg>
      <div><h3>One company for everyone</h3><p>We are a service provider for doctors and hospitals!</p></div>
    </div>
    <div class="point" style="top:148px">
      <svg width="38" height="38" viewBox="0 0 38 38" fill="none" stroke="#0c4ea3" stroke-width="2"><rect x="3" y="11" width="32" height="22" rx="2"/><path d="M13 11V6h12v5M3 20h32M17 18h4v5h-4z"/></svg>
      <div><h3>Experience characterises us</h3><p>Our team has many years of experience in the business field!</p></div>
    </div>
    <div class="point" style="top:226px">
      <svg width="38" height="38" viewBox="0 0 38 38" fill="none" stroke="#0c4ea3" stroke-width="2"><path d="M8 3h16l6 6v26H8z"/><path d="M13 13h10M13 19h8"/><path d="M22 30c-4-3-6-5-4-7 1-1 3-1 4 1 1-2 3-2 4-1 2 2 0 4-4 7z"/></svg>
      <div><h3>The product is close to our hearts</h3><p>We repair and sell second hand, flexible endoscopes!</p></div>
    </div>
    <div class="point" style="top:306px">
      <svg width="38" height="38" viewBox="0 0 38 38" fill="none" stroke="#0c4ea3" stroke-width="2"><path d="M19 3l13 5v10c0 8-6 14-13 17-7-3-13-9-13-17V8z"/><path d="M13 19l4 4 8-8"/></svg>
      <div><h3>Guaranteed service</h3><p>You receive a six-month warranty on all repairs!</p></div>
    </div>
    <div class="point" style="top:379px">
      <svg width="38" height="38" viewBox="0 0 38 38" fill="none" stroke="#0c4ea3" stroke-width="2"><circle cx="19" cy="16" r="13"/><path d="M14 20v-6l4-5c1-1 3 0 2 2v3h5l-1 6zM4 35h6M16 35h6M28 35h6"/></svg>
      <div><h3>Quality not quantity</h3><p>Reliability and durability instead of inferior replacements!</p></div>
    </div>
    <div class="point" style="top:458px">
      <svg width="38" height="38" viewBox="0 0 38 38" fill="none" stroke="#0c4ea3" stroke-width="2"><circle cx="19" cy="19" r="7"/><circle cx="19" cy="4" r="3"/><circle cx="19" cy="34" r="3"/><circle cx="4" cy="19" r="3"/><circle cx="34" cy="19" r="3"/><circle cx="8" cy="8" r="3"/><circle cx="30" cy="30" r="3"/><circle cx="30" cy="8" r="3"/><circle cx="8" cy="30" r="3"/></svg>
      <div><h3>Services for everyone</h3><p>Our service includes the manufacturers Olvara,<br>Pentrix and Fujiro!</p></div>
    </div>
  </div>
</section>

<footer class="section footer">
  <a class="abs footer-brand" href="https://lumenfix.example/en/lumenfix-english/"><span class="brand-dot"></span>LumenFix</a>
  <div class="abs fcol" style="left:473px">
    <h4>Menu</h4>
    <a href="https://lumenfix.example/en/lumenfix-english/">Home</a>
    <a href="#">Endoscope repair</a>
    <a href="https://lumenfix.example/en/used-endoscopes/">Used endoscopes</a>
    <a href="#">Endoscopy systems</a>
    <a href="#">Endoscopy accessories</a>
    <a href="https://lumenfix.example/en/purchase/">Purchase</a>
  </div>
  <div class="abs fcol" style="left:740px">
    <h4>Links</h4>
    <a href="#">Informations</a>
    <a href="#">About us</a>
    <a href="#">Contact us</a>
    <a href="#">TOS</a>
    <a href="#">Copyrights</a>
    <a href="#">Privacy policy</a>
  </div>
  <div class="abs fcol" style="left:948px">
    <h4>Follow us</h4>
    <div class="fsocial"><span class="social-dot" aria-label="Social profile"></span><span class="social-sq" aria-label="Social profile"></span></div>
  </div>
  <div class="abs rule"></div>
  <div class="abs copy">© 2022 LumenFix GmbH</div>
</footer>

</body>
</html>
```